Flyer-Design für Audio und Video Installationen
Zielgruppe
Die Firma Kellerhof Audio und Video Installationen wurde im Jahr 1997 von Matthias Kellerhof gegründet und im Handelsregister eingetragen. In der Anfangszeit waren wir als Subunternehmer der Firma orvi-netlink tätig und haben massgeblich zur Sanierung der hausinternen Verkabelung im Raum Winterthur beigetragen.
Auch im Bereich des TV- und Radioempfangs via Parabolantenne sind wir Ihr Spezialist – vom Einfamilienhaus mit einem oder mehreren Empfangsgeräten, bis zu grossen Überbauungen oder Hotelanlagen mit Satellitenaufbereitungsanlagen.
In den ersten Stunden von Fiber to the home (FTTH) im Jahr 2010, wurden wir angefragt, die ersten Glasfaser-anschlüsse im Auftrag der Telvora zu realisieren. Seither arbeiten permanent 3 – 4 unserer Teams im Auftrag der Telvora und der Gemeindewerk Lindmatt für die Erstellung von FTTH Anschlüssen.
Ausserdem sind wir im Bereich Industrie, Banken und Versicherungen für verschiedene Partner im Einsatz um LWL-Installationen zu planen und zu erstellen, sowohl Multimode als auch Singlemode.
Kellerhof Audio und Video Installationen ist ein Kleinbetrieb mit momentan 10 Mitarbeitern aus den Bereichen Multimediaelektroniker und Elektromonteure.
Wir sind durch unsere Begeisterung für die neueste Technik, durch die tägliche Praxis und viele Weiter-bildungen trotz des schnellen Wandels der heutigen Technik stets auf dem neuesten Stand.
Aufgabenstellung
Das Hauptaugenmerk sollte auf Glasfaser, FTTH, LumaKet,c Installationen liegen. Eventuell möchte ich noch ein Angebot/Dienstleistung mit Preis Platzieren. OTO Dose (Glasfasersteckdose) vom Kommunikationsverteiler in ein anderes Zimmer verlegen, da in diesen Verteiler oft zuwenig Platz ist für Modem, Router etc.

```html
<!DOCTYPE html>
<html lang="de">
<head>
<meta charset="utf-8">
<title>Kellerhof Flyer DIN lang</title>
<link href="https://fonts.googleapis.com/css2?family=Roboto:wght@300;400;500;700&family=Roboto+Mono:wght@500&display=swap" rel="stylesheet">
<style>
:root{
  --green:#5b9a3c;
  --band:#c9c9c9;
  --ink:#1e1e1e;
  --text:#555;
  --pale:#eff1e7;
  --photo-a:#7f9aa6;
  --photo-b:#3e4b55;
  --frame:#d8d8d8;
  --slot:#efefef;
}
*{box-sizing:border-box;margin:0;padding:0}
html,body{width:930px;height:1200px;overflow:hidden;background:#fff}
body{position:relative;font-family:'Roboto',sans-serif;color:var(--text)}
.label{position:absolute;font-size:13px;color:var(--ink);font-weight:400;white-space:nowrap}
.spread{position:absolute;left:75px;width:780px;height:552px;display:flex;flex-direction:column;box-shadow:0 2px 6px rgba(0,0,0,.25);background:#fff}
.spread-outer{top:36px}
.spread-inner{top:632px}
.band-top{height:22px;background:var(--band)}
.band-bottom{height:14px;background:var(--band)}
.panels{flex:1;display:flex}
.panel{position:relative;border-right:1px solid var(--frame);overflow:hidden}
.panel:last-child{border-right:none}
.spread-outer .p1{width:256px}.spread-outer .p2{width:262px}.spread-outer .p3{width:262px}
.spread-inner .p1{width:264px}.spread-inner .p2{width:263px}.spread-inner .p3{width:253px}
.pad{padding:16px 14px 0}
h2{font-size:14px;font-weight:500;letter-spacing:1px;color:var(--ink);margin-bottom:12px;line-height:1.2}
h2.mono{font-family:'Roboto Mono',monospace;font-size:13px;letter-spacing:.5px}
p{font-size:9px;line-height:1.42;font-weight:300}
p b{font-weight:500;color:#333}
.service{margin-top:9px}
.service h3{font-size:12.5px;font-weight:400;color:var(--green);display:flex;align-items:center;gap:5px;margin-bottom:2px}
.service h3 i{display:inline-block;width:9px;height:9px;background:var(--green)}
.brand{display:flex;align-items:center;gap:6px;font-weight:500;color:var(--ink)}
.brand .dot{display:inline-block;border-radius:50%;background:var(--green)}
.brand-s{margin-top:16px;font-size:11px}
.brand-s .dot{width:8px;height:8px}
.brand-m{margin:10px 0 22px;font-size:12px}
.brand-m .dot{width:9px;height:9px}
.brand-l{justify-content:center;margin-top:52px;font-size:20px}
.brand-l .dot{width:14px;height:14px}
.contact p{font-size:9px}
.contact .gap{margin-top:10px}
.web{position:absolute;bottom:10px;left:0;right:0;text-align:center;color:var(--green);font-size:11px;font-weight:500}
.photo{height:179px;background:linear-gradient(135deg,var(--photo-a),#9aa9b0 40%,var(--photo-b))}
.topics{font-size:10px;color:var(--ink);text-align:center;margin-top:10px}
.spread-inner .p1 .pad p+p{margin-top:10px}
.white-top{height:242px}
.pale-bottom{position:absolute;left:0;right:0;bottom:0;top:242px;background:var(--pale)}
.green-box{height:311px;background:var(--green);padding:12px 12px 0}
.green-box p{color:#fff;font-weight:300}
.spacer{float:right;width:0;height:121px}
.img-slot{float:right;clear:right;width:126px;height:168px;background:var(--slot);margin-left:6px}
.p3 .pale-bottom{top:311px;padding:14px 12px 0}
.p2 .pale-bottom{padding:16px 14px 0}
</style>
</head>
<body>

<div class="label" style="left:112px;top:12px">Seite 5 | eingeklappte Seite</div>
<div class="label" style="left:399px;top:12px">Seite 6 | Rückseite</div>
<div class="label" style="left:665px;top:12px">Seite 1 | Titelseite</div>

<section class="spread spread-outer">
  <div class="band-top"></div>
  <div class="panels">
    <article class="panel p1">
      <div class="pad">
        <h2>DIENSTLEISTUNGEN</h2>
        <p><b>Seit 1997</b> sind wir Ihr <b>Ansprechpartner für Installationen</b> in den Bereichen <b>Satellitenempfang, Kabelfernsehen, Multimedia</b> und <b>Glasfasertechnik – Fiber to the Home</b> im Kanton Zürich und Umgebung. In kleinen, gut eingespielten Teams sind wir im schnellen Wandel der heutigen Technik durch Weiterbildungen <b>stets auf dem neuesten Stand.</b></p>
        <div class="service">
          <h3><i></i>Satellitenempfang</h3>
          <p>Vom <b>Einfamilienhaus</b> mit einem oder mehreren Empfangsgeräten, bis hin zu <b>grossen Überbauungen</b> oder <b>Hotelanlagen mit Satellitenaufbereitung</b> – wir bieten das nötige <b>Know-how.</b></p>
        </div>
        <div class="service">
          <h3><i></i>Fiber to the Home (FTTH)</h3>
          <p>Im Auftrag der <b>Telvora</b> und der <b>Gemeindewerk Lindmatt</b> sind wir als <b>Partner verschiedener Firmen</b> für <b>Glasfaserinstallationen</b> vom Hauseinführungspunkt bis in die Wohnung im Einsatz.</p>
        </div>
        <div class="service">
          <h3><i></i>Kabelfernsehen</h3>
          <p>Seit Jahren arbeiten wir im <b>orvi-netlink Netz.</b> Beim Erweitern oder Modernisieren Ihrer Kabelfernsehanlage sind wir Ihr <b>kompetenter Ansprechpartner.</b></p>
        </div>
        <div class="service">
          <h3><i></i>LWL Installationen</h3>
          <p>Ob <b>Singlemode</b> oder <b>Multimode, Glasfaserinstallationen</b> für <b>Gewerbe, Banken</b> und <b>Versicherungen,</b> mit uns haben Sie den <b>richtigen Partner</b> um eine <b>professionelle Installation</b> zu realisieren.</p>
        </div>
        <div class="brand brand-s"><span class="dot"></span>Kellerhof</div>
      </div>
    </article>

    <article class="panel p2">
      <div class="pad contact">
        <h2>KONTAKT</h2>
        <div class="brand brand-m"><span class="dot"></span>Kellerhof</div>
        <p><b>Kellerhof Audio und Video Installationen</b><br>Lindenmattstrasse 12<br>CH-8699 Lindmatt<br>Telefon: 044 555 01 23<br>info@kellerhof-av.ch<br>www.kellerhof-av.ch</p>
        <p class="gap"><b>Bürozeiten:</b><br>Montag–Freitag<br>7:00 Uhr–18:00 Uhr</p>
      </div>
      <div class="web">www.kellerhof-av.ch</div>
    </article>

    <article class="panel p3">
      <div class="photo" role="img" aria-label="Nahaufnahme von Koaxialsteckern an einem Verteiler"></div>
      <div class="topics">GLASFASER | SATELLIT | KABEL | MULTIMEDIA</div>
      <div class="brand brand-l"><span class="dot"></span>Kellerhof</div>
      <div class="web">www.kellerhof-av.ch</div>
    </article>
  </div>
  <div class="band-bottom"></div>
</section>

<div class="label" style="left:345px;top:608px">Seite 2, Seite 3, Seite 4 | Innenseiten</div>

<section class="spread spread-inner">
  <div class="band-top"></div>
  <div class="panels">
    <article class="panel p1">
      <div class="pad">
        <h2>SEIT ÜBER 20 JAHREN UNTER-<br>WEGS FÜR UNSERE KUNDEN</h2>
        <p>Die Firma <b>Kellerhof Audio und Video Installationen</b> wurde <b>im Jahr 1997</b> von <b>Matthias Kellerhof</b> gegründet und im Handelsregister eingetragen. In der Anfangszeit waren wir als Subunternehmer der Firma orvi-netlink tätig und haben massgeblich zur Sanierung der hausinternen Verkabelung im Raum Winterthur beigetragen.</p>
        <p>Auch im Bereich des <b>TV- und Radioempfangs via Parabolantenne</b> sind wir <b>Ihr Spezialist</b> – vom <b>Einfamilienhaus</b> mit einem oder mehreren Empfangsgeräten, bis zu grossen Überbauungen oder Hotelanlagen mit Satellitenaufbereitungsanlagen.</p>
        <p>In den ersten Stunden von Fiber to the home (FTTH) im Jahr 2010, wurden wir angefragt, die ersten Glasfaser-anschlüsse im Auftrag der Telvora zu realisieren. Seither arbeiten permanent 3 – 4 unserer Teams im Auftrag der Telvora und der Gemeindewerk Lindmatt für die Erstellung von FTTH Anschlüssen.</p>
        <p>Ausserdem sind wir im Bereich Industrie, Banken und Versicherungen für verschiedene Partner im Einsatz um LWL-Installationen zu planen und zu erstellen, sowohl Multimode als auch Singlemode.</p>
        <p>Kellerhof Audio und Video Installationen ist ein Kleinbetrieb mit momentan 10 Mitarbeitern aus den Bereichen Multimediaelektroniker und Elektromonteure.</p>
        <p>Wir sind durch unsere Begeisterung für die neueste Technik, durch die tägliche Praxis und viele Weiter-bildungen trotz des schnellen Wandels der heutigen Technik stets auf dem neuesten Stand.</p>
      </div>
    </article>

    <article class="panel p2">
      <div class="pad white-top">
        <h2 class="mono">XXXXXX XXX<br>XXXX XXXXXXX</h2>
        <p>Ugias eos et officae et re voluptur re ium voluptae volum ab imporit, et laut exped quis denitam quaest quisquate nient, cuptia cum sit ex earchilles magnia tiorem es nos magnis si offictus sam recatus exeress inctemquodis ma que vendus.<br>Bis sunt qui odi occusam ideleni storessime re nus cum laut reius as autemqu iaturis ut venditat et hit fugia in repreptatus es vendeli berspici num res etus ma accabor emporep erundel lendis mo totaque idis quia volupturia et autem renimo mod quo comnimus sita cum assenem as dolorpo raerita idescia quasinci lia sa volore, quid mil idebita sperunt opta prat. Doloraectemo esti tendipi taessin conseque volupis</p>
      </div>
      <div class="pale-bottom">
        <h2 class="mono">XXXXXX XXX XXXXXXX</h2>
        <p>Epero voluptati utas ducidunt fuga. Nus, cupiduntint evenis ma doluptat.<br>Tis aut exceatat fuga. Nequiberunt quaspero mosandi pictem eiuntur?<br>Et quat. Ati quam volore mo que verit eos et labo. Hendi cusaper speliquias et lab ipsam ex evella ped qui odi dia volupta non pro oditat fuga. Ut porepercid excepremporе lam volupta cullessi bea cullaceptios unt, coris et mi, quat am quate simusam quamus verupta nate il magnis aceatur alit ea dolupti si nobiste pro essimusam etustibus et volorporio voluptatum sant voluptat rehenihilis quam ipsusam culla quunde re nobis del everum vendellore plaborestior repudi cum asim et volupiet quisci te volor sitis de ad et faceped eum vendaerunt eturiaecti aut etur rem nihillaudani nem volut omnimpo repedigent ium si</p>
      </div>
    </article>

    <article class="panel p3">
      <div class="green-box">
        <div class="spacer"></div>
        <div class="img-slot" role="img" aria-label="Platz für ein Produktbild der Glasfasersteckdose"></div>
        <p>Nam, sint es alitaque demquos pa aut aces cum eum digenihilit ius.<br>Di od ullique cone nis a volute quissim illuptatio. Debis modi qui a nobit, quatis nos dustiat et eum nonecab oreprae et, sus rest quasi odi dolut magnitatum repe quam re, volor alis denecae. Nequist et quaspiciat.<br>Harchil is esequi de aut aciat.<br>Tate voluptatis remporeris antem ut prat quatum si comnis et re liquidi genihil modipsam que ma sed ut fuga. Itas et undis eum eatur? Quis aut acit, optam expeditas explaborro molore vitaqunt adi sum dolorro etur? Soluptam hiliquae. Et maio offic to es ellisqui volum quid enitati vellupta sime vid ea</p>
      </div>
      <div class="pale-bottom">
        <p>oditiaes eosam, estrum, corerovid eveliquas voluptae doluptiis solest, nonse mo de velest voluptas idunt in nonserr ovitatem quam eatiori aspidel ignimus apelest lautem faccaborem eum que magnist el invero testotas que a dolo blanihi litiatur?<br>Sa poribus doluptatur, veribus, quis corum im nonsed ent.<br>Et lit enimin cusdaepudi de nia se es dolumquunt quibuscit parum numquia dolut et ut exerit et que aborenditisi rem quiae resti ne sitis esseceperum simpor rectatemque namet, sandestem et, volupta tesenis ea conempo ratquam, ut explaborere cupitionest ilit</p>
      </div>
    </article>
  </div>
  <div class="band-bottom"></div>
</section>

</body>
</html>
```